Company Website

We require an online clothing store website for construction workwear.
It needs to be easy to read, user friendly, easy to navigate purchasing.
We are after designs incorporating our recently design logo, and colour combinations black white and orange (same as the company logo). Needs to highlight quality, safety and products. Any ideas around highlighting branding are welcome.

Target Market(s)

Construction workers and businesses.

Industry/Entity Type

Construction

Coding

Coded - Design and coding required

Number of Pages Required

5+ page

Colors
EE7325
F08F49
F5BC92
FAE3D3
FDF4ED

Requirements
Must have
• Include all pictures, prices and details of the products we sell. See PDF uploaded to brief.
Nice to have
• Simple access to purchase items. Easy to navigate website layout.

```html
<!DOCTYPE html>
<html lang="en">
<head>
<meta charset="utf-8">
<title>Guardline Site Workwear</title>
<link href="https://fonts.googleapis.com/css2?family=Orbitron:wght@600;700;800&family=Montserrat:wght@400;500;600;700&display=swap" rel="stylesheet">
<style>
:root{
  --orange:#e8541a;
  --orange-soft:#ee7325;
  --peach:#f5bc92;
  --ink:#1f1f1f;
  --dark:#262626;
  --navy:#1c2a44;
  --grey:#5b5b5b;
  --light:#f1f1f1;
  --white:#ffffff;
  --stage:#e6e6e6;
}
*{box-sizing:border-box;margin:0;padding:0}
html,body{width:1200px;height:3634px;overflow:hidden}
body{background:var(--stage);font-family:"Montserrat",sans-serif;color:var(--ink)}
.site{position:absolute;top:239px;left:0;width:1200px;background:var(--white)}
section,header,footer{position:relative;width:1200px;overflow:hidden}
.display{font-family:"Orbitron",sans-serif;font-weight:700;text-transform:uppercase;letter-spacing:2px}
.btn{display:inline-block;font-family:"Montserrat",sans-serif;font-weight:700;font-size:10px;letter-spacing:1.5px;text-transform:uppercase;padding:9px 18px;color:var(--white)}
.btn-grey{background:#5a5a5a}
.btn-orange{background:var(--orange)}
.btn-dark{background:#3a3a3a}

/* header */
.topbar{height:75px;display:flex;align-items:center}
.nav{position:absolute;left:100px;top:25px;display:flex;gap:6px;align-items:center}
.nav a{font-size:11px;font-weight:600;letter-spacing:1px;color:#333;text-decoration:none;padding:7px 12px;text-transform:uppercase}
.nav a.active{background:var(--orange);color:var(--white)}
.brand{position:absolute;left:0;right:0;top:16px;text-align:center}
.brand-name{font-family:"Orbitron",sans-serif;font-weight:800;font-size:30px;color:var(--orange);letter-spacing:2px;line-height:1}
.brand-tag{font-family:"Orbitron",sans-serif;font-weight:800;font-size:10px;color:var(--orange);letter-spacing:5px;margin-top:4px}
.tools{position:absolute;left:838px;top:24px;display:flex;gap:8px;align-items:center}
.search{width:143px;height:26px;border:1px solid #ddd;font-size:10px;color:#999;display:flex;align-items:center;justify-content:space-between;padding:0 8px}
.iconbox{width:26px;height:26px;border:1px solid #ddd;display:flex;align-items:center;justify-content:center}
.cart{height:26px;border:1px solid #ddd;font-size:11px;display:flex;align-items:center;gap:6px;padding:0 10px}

/* hero */
.hero{height:500px;background:#1d2530}
.hero-photo{position:absolute;inset:0;background:radial-gradient(ellipse at 72% 45%,#d9741f 0%,#a24c17 22%,#3a3a3c 48%,#1b222c 75%)}
.hero-copy{position:absolute;left:100px;top:130px}
.hero-kicker{font-size:24px;color:var(--orange-soft);line-height:1.2}
.hero-title{font-size:50px;color:var(--white);line-height:1.1;margin-top:20px;font-weight:800}
.hero-title span{color:var(--orange)}
.hero-copy .btn{margin-top:22px}

/* perks */
.perks{height:119px;background:var(--orange);display:flex;justify-content:center;align-items:center;gap:96px}
.perk{display:flex;align-items:center;gap:12px;color:var(--white)}
.perk-icon{width:54px;height:54px;border-radius:50%;background:var(--white);display:flex;align-items:center;justify-content:center}
.perk h4{font-family:"Orbitron",sans-serif;font-size:14px;letter-spacing:1.5px;font-weight:700}
.perk p{font-size:12px;margin-top:3px}

/* products */
.products{height:559px;text-align:center}
.section-title{font-size:28px;color:var(--orange);letter-spacing:3px}
.products .section-title{padding-top:66px}
.cards{position:absolute;top:132px;left:150px;display:flex;gap:27px}
.card{width:205px}
.card-box{height:235px;border:1px solid #e5e5e5;position:relative}
.card-img{position:absolute;left:35px;top:25px;width:135px;height:160px;border-radius:6px}
.card-bag{position:absolute;right:8px;bottom:8px;width:22px;height:22px;border:1px solid #ccc;display:flex;align-items:center;justify-content:center}
.card-bag.hot{background:var(--orange);border-color:var(--orange)}
.card-name{font-size:11px;margin-top:10px;line-height:1.45;color:#333}
.card-price{font-size:11px;color:#888;margin-top:4px}
.card-price b{color:var(--orange)}
.card.active .card-box{box-shadow:0 4px 14px rgba(0,0,0,.12)}
.card.active .card-meta{border-bottom:3px solid var(--orange);padding-bottom:8px}
.products .btn{position:absolute;left:555px;top:471px}

/* about */
.about{height:520px;background:#efefef}
.about svg.bg{position:absolute;inset:0}
.about-photo{position:absolute;left:100px;top:74px;width:454px;height:370px;background:linear-gradient(135deg,#e9e4dc 0%,#d6c9b6 45%,#2f6bc4 75%,#1d4f9e 100%)}
.about-copy{position:absolute;left:632px;top:140px;width:370px}
.about-copy .section-title{font-size:28px}
.about-copy h3{font-size:14px;font-weight:700;line-height:1.45;margin-top:18px}
.about-copy p{font-size:11px;line-height:1.5;color:#444;margin-top:12px}
.about-copy .btn{margin-top:16px}

/* safety */
.safety{height:414px;background:var(--dark)}
.safety svg.bg{position:absolute;inset:0}
.safety-photo{position:absolute;inset:0}
.safety-copy{position:absolute;left:100px;top:110px;width:300px;color:var(--white)}
.safety-copy h2{font-size:34px;color:var(--orange);line-height:1.1;font-weight:800}
.safety-copy p{font-size:18px;line-height:1.35;margin-top:16px}
.safety-copy .btn{margin-top:18px}
.thumb{position:absolute;background:var(--white);padding:6px}
.thumb div{width:100%;height:100%}

/* testimonials */
.testimonials{height:570px;text-align:center}
.testimonials .section-title{padding-top:66px}
.quote-mark{width:44px;height:44px;border-radius:50%;background:#3a3a3a;margin:26px auto 0;display:flex;align-items:center;justify-content:center;color:var(--white);font-family:Georgia,serif;font-size:28px;font-weight:700;line-height:1}
.quote{width:700px;margin:22px auto 0;font-size:13px;line-height:1.45;color:#333}
.author{display:flex;justify-content:center;align-items:center;gap:10px;margin-top:22px;text-align:left}
.avatar{width:38px;height:38px;border-radius:50%;background:linear-gradient(135deg,#e7c9ad,#b88562)}
.author b{display:block;font-size:11px;color:var(--orange);font-weight:600}
.author span{font-size:11px;color:#555}
.dots{display:flex;justify-content:center;gap:8px;margin-top:26px}
.dots i{width:9px;height:9px;border-radius:50%;border:1px solid #999}
.dots i.on{border:2px solid var(--orange);width:11px;height:11px;margin-top:-1px}
.cta{position:absolute;left:240px;top:456px;width:720px;height:161px;background:var(--white);box-shadow:0 6px 20px rgba(0,0,0,.15);z-index:2;display:flex}
.cta-copy{padding:36px 0 0 24px;width:330px;background:var(--white)}
.cta-copy h3{font-size:17px;line-height:1.3;color:#333;letter-spacing:2px}
.cta-copy .btn{margin-top:14px}
.cta-photo{flex:1;background:linear-gradient(90deg,#ffffff 0%,#7a7a70 25%,#3f4a33 60%,#b9d34a 85%,#2e3320 100%)}

/* footer */
.footer{height:368px;background:#1c1c1c;color:#ddd}
.footer-brand{position:absolute;left:100px;top:104px}
.footer-brand .brand-name{font-size:30px}
.footer-brand .brand-tag{font-size:10px;text-align:right}
.pay{display:flex;gap:8px;margin-top:18px}
.pay i{width:30px;height:30px;border-radius:50%;border:2px solid var(--white)}
.col{position:absolute;top:100px}
.col h5{font-family:"Orbitron",sans-serif;font-size:12px;color:var(--orange);letter-spacing:2px;margin-bottom:16px}
.col li{list-style:none;font-size:11px;margin-bottom:9px}
.col li.current{color:var(--orange);text-decoration:underline}
.contact-row{display:flex;gap:10px;align-items:flex-start;font-size:11px;margin-bottom:16px;line-height:1.35}
.subscribe{position:absolute;top:280px;left:100px;right:100px}
.subscribe h5{font-family:"Orbitron",sans-serif;font-size:13px;color:var(--orange);letter-spacing:2px}
.subscribe p{font-size:10px;margin-top:4px}
.sub-form{position:absolute;left:390px;top:0;display:flex}
.sub-input{width:410px;height:32px;border:1px solid #444;background:#222;color:#999;font-size:10px;display:flex;align-items:center;padding:0 14px}
.sub-btn{width:106px;height:32px;background:#444;color:var(--white);font-size:10px;font-weight:700;letter-spacing:1px;display:flex;align-items:center;justify-content:center}
.bottom{height:31px;background:var(--orange);color:var(--white);font-size:10px;display:flex;align-items:center;justify-content:space-between;padding:0 100px}
.social{display:flex;gap:8px}
.social i{width:14px;height:14px;background:var(--white);opacity:.9}
.social i.on{background:var(--white);outline:2px solid var(--white);opacity:1}
</style>
</head>
<body>
<div class="site">

  <header class="topbar">
    <nav class="nav">
      <a class="active">Home</a><a>About</a><a>Shop</a><a>Contact</a>
    </nav>
    <div class="brand">
      <div class="brand-name">GUARDLINE</div>
      <div class="brand-tag">SITE WORKWEAR</div>
    </div>
    <div class="tools">
      <div class="search">Search
        <svg width="11" height="11" viewBox="0 0 12 12"><circle cx="5" cy="5" r="4" fill="none" stroke="#555" stroke-width="1.4"/><line x1="8" y1="8" x2="11" y2="11" stroke="#555" stroke-width="1.4"/></svg>
      </div>
      <div class="iconbox"><svg width="12" height="12" viewBox="0 0 12 12"><circle cx="6" cy="4" r="2.5" fill="none" stroke="#444" stroke-width="1.2"/><path d="M1.5 11.5c0-3 2-4.5 4.5-4.5s4.5 1.5 4.5 4.5" fill="none" stroke="#444" stroke-width="1.2"/></svg></div>
      <div class="cart"><svg width="11" height="12" viewBox="0 0 11 12"><rect x="1" y="4" width="9" height="7.5" fill="var(--orange)"/><path d="M3 4V3a2.5 2.5 0 0 1 5 0v1" fill="none" stroke="var(--orange)" stroke-width="1.2"/></svg>$ 0.00</div>
    </div>
  </header>

  <section class="hero">
    <div class="hero-photo" role="img" aria-label="Close view of a worker in an orange and navy hi-vis jacket against a dark background"></div>
    <div class="hero-copy">
      <div class="hero-kicker display">Construction<br>Workwear</div>
      <div class="hero-title display"><span>C</span>lothing<br><span>S</span>tore</div>
      <a class="btn btn-grey">Shop Now</a>
    </div>
  </section>

  <section class="perks">
    <div class="perk">
      <div class="perk-icon"><svg width="28" height="20" viewBox="0 0 28 20"><rect x="1" y="3" width="16" height="11" fill="none" stroke="#777" stroke-width="1.5"/><path d="M17 7h6l4 4v3H17z" fill="none" stroke="#777" stroke-width="1.5"/><circle cx="6" cy="16" r="2.5" fill="#fff" stroke="#777" stroke-width="1.5"/><circle cx="21" cy="16" r="2.5" fill="#fff" stroke="#777" stroke-width="1.5"/></svg></div>
      <div><h4>FREE SHIPPING</h4><p>Free Shipping World Wide</p></div>
    </div>
    <div class="perk">
      <div class="perk-icon"><svg width="26" height="26" viewBox="0 0 26 26"><circle cx="13" cy="11" r="8" fill="none" stroke="#777" stroke-width="1.5"/><text x="13" y="15" font-size="10" text-anchor="middle" fill="#777" font-family="Montserrat,sans-serif" font-weight="700">$</text><path d="M3 22h20" stroke="#777" stroke-width="1.5"/></svg></div>
      <div><h4>CASH BACK</h4><p>10 Days for Free Returns</p></div>
    </div>
    <div class="perk">
      <div class="perk-icon"><svg width="26" height="26" viewBox="0 0 26 26"><path d="M5 14v-2a8 8 0 0 1 16 0v2" fill="none" stroke="#777" stroke-width="1.5"/><rect x="3" y="13" width="4" height="7" rx="1" fill="#777"/><rect x="19" y="13" width="4" height="7" rx="1" fill="#777"/><path d="M21 20c0 2-2 3-5 3" fill="none" stroke="#777" stroke-width="1.5"/></svg></div>
      <div><h4>ONLINE SUPPORT</h4><p>24/7 Customer Online Support</p></div>
    </div>
  </section>

  <section class="products">
    <h2 class="section-title display">Product Range</h2>
    <div class="cards">
      <article class="card">
        <div class="card-box">
          <div class="card-img" role="img" aria-label="Orange long-sleeve vented work shirt with reflective tape" style="background:linear-gradient(180deg,#ff6d1a,#f2550c)"></div>
          <div class="card-bag"><svg width="10" height="11" viewBox="0 0 10 11"><rect x="1" y="3.5" width="8" height="7" fill="none" stroke="#666"/><path d="M3 3.5V2.5a2 2 0 0 1 4 0v1" fill="none" stroke="#666"/></svg></div>
        </div>
        <div class="card-meta"><div class="card-name">Mens L/S Standard Vented<br>Orange Shirt</div><div class="card-price">Start Price: <b>$43.95ea</b></div></div>
      </article>
      <article class="card active">
        <div class="card-box">
          <div class="card-img" role="img" aria-label="Two-toned yellow and navy taped work shirt" style="background:linear-gradient(180deg,#f5e21a 0%,#f5e21a 50%,#1f2c5a 52%,#1f2c5a 100%)"></div>
          <div style="position:absolute;left:8px;bottom:8px;display:flex;gap:4px"><i style="width:20px;height:20px;border:1px solid #ccc;background:linear-gradient(180deg,#f26a12 50%,#1f2c5a 50%)"></i><i style="width:20px;height:20px;border:1px solid #ccc;background:linear-gradient(180deg,#f5e21a 50%,#1f2c5a 50%)"></i></div>
          <div class="card-bag hot"><svg width="10" height="11" viewBox="0 0 10 11"><rect x="1" y="3.5" width="8" height="7" fill="none" stroke="#fff"/><path d="M3 3.5V2.5a2 2 0 0 1 4 0v1" fill="none" stroke="#fff"/></svg></div>
        </div>
        <div class="card-meta"><div class="card-name">Mens L/S Two-Toned Vented<br>Taped Shirt</div><div class="card-price">Start Price: <b>$43.95ea</b></div></div>
      </article>
      <article class="card">
        <div class="card-box">
          <div class="card-img" role="img" aria-label="Navy hi-vis work pants with reflective hoops" style="left:60px;width:85px;background:linear-gradient(180deg,#1d2d5c,#14204a)"></div>
          <div class="card-bag"><svg width="10" height="11" viewBox="0 0 10 11"><rect x="1" y="3.5" width="8" height="7" fill="none" stroke="#666"/><path d="M3 3.5V2.5a2 2 0 0 1 4 0v1" fill="none" stroke="#666"/></svg></div>
        </div>
        <div class="card-meta"><div class="card-name">Hi-Vis Navy Pants - Double<br>Hoop</div><div class="card-price">Start Price: <b>$47.00ea</b></div></div>
      </article>
      <article class="card">
        <div class="card-box">
          <div class="card-img" role="img" aria-label="Lime and navy hi-vis long-sleeve polo" style="background:linear-gradient(180deg,#c6f22d 0%,#c6f22d 55%,#1c2540 57%,#1c2540 100%)"></div>
          <div class="card-bag"><svg width="10" height="11" viewBox="0 0 10 11"><rect x="1" y="3.5" width="8" height="7" fill="none" stroke="#666"/><path d="M3 3.5V2.5a2 2 0 0 1 4 0v1" fill="none" stroke="#666"/></svg></div>
        </div>
        <div class="card-meta"><div class="card-name">Hi- Vis L/S Polo</div><div class="card-price">Start Price: <b>$43.95ea</b></div></div>
      </article>
    </div>
    <a class="btn btn-dark">View All</a>
  </section>

  <section class="about">
    <svg class="bg" width="1200" height="520" viewBox="0 0 1200 520">
      <polygon points="0,0 352,0 620,520 0,520" fill="var(--navy)"/>
      <polygon points="352,0 385,0 650,520 620,520" fill="var(--peach)"/>
    </svg>
    <div class="about-photo" role="img" aria-label="Seamstress working at a sewing machine on blue fabric"></div>
    <div class="about-copy">
      <h2 class="section-title display">About Us</h2>
      <h3>Lorem Ipsum is simply dummy text of the printing and typesetting industry.</h3>
      <p>Lorem Ipsum is simply dummy text of the printing and typesetting industry. Lorem Ipsum has been the industry's standard dummy text ever since the 1500s, when an unknown printer took a galley of type and scrambled it to make a type specimen book. It has survived not only five centuries, but also the leap into electronic typesetting, remaining essentially unchanged.</p>
      <a class="btn btn-orange">Read More</a>
    </div>
  </section>

  <section class="safety">
    <svg class="bg" width="1200" height="414" viewBox="0 0 1200 414">
      <polygon points="540,0 1200,0 1200,414 660,414" fill="#6f88a8"/>
    </svg>
    <div class="safety-photo" role="img" aria-label="Two construction workers in hard hats and orange hi-vis vests on a building site" style="clip-path:polygon(540px 0,1200px 0,1200px 414px,660px 414px);background:linear-gradient(100deg,#8ba1bd 0%,#c7d3e0 35%,#e8772a 60%,#d4621d 80%,#5a4636 100%)"></div>
    <div class="safety-copy">
      <h2 class="display"><span style="color:var(--orange)">Safety<br>First</span></h2>
      <p>Protect yourself by being visible at all times with high vis workwear in all forms.</p>
      <a class="btn btn-grey">Shop Now</a>
    </div>
    <div class="thumb" style="left:516px;top:90px;width:102px;height:102px"><div role="img" aria-label="Orange and lime hi-vis shirts" style="background:linear-gradient(90deg,#f26a12 50%,#c6f22d 50%)"></div></div>
    <div class="thumb" style="left:590px;top:210px;width:134px;height:122px"><div role="img" aria-label="Two-toned hi-vis work shirts" style="background:linear-gradient(90deg,#f26a12 0%,#1f2c5a 50%,#f5e21a 100%)"></div></div>
  </section>

  <section class="testimonials">
    <h2 class="section-title display">Testimonials</h2>
    <div class="quote-mark">&ldquo;</div>
    <p class="quote">Lorem Ipsum is simply dummy text of the printing and typesetting industry. Lorem Ipsum has been the industry's standard dummy text ever since the 1500s, when an unknown printer took a galley of type and scrambled it to make a type specimen book. It has survived not only five centuries, but also the leap into electronic typesetting, remaining essentially unchanged.</p>
    <div class="author">
      <div class="avatar" role="img" aria-label="Customer portrait"></div>
      <div><b>J R Mallory</b><span>Lorem Ipsum</span></div>
    </div>
    <div class="dots"><i></i><i></i><i class="on"></i><i></i></div>
    <div class="cta">
      <div class="cta-copy">
        <h3 class="display">Let us guide<br>you in your choice<br>of workwear</h3>
        <a class="btn btn-dark">Check out our guides</a>
      </div>
      <div class="cta-photo" role="img" aria-label="Workers in hi-vis vests on site"></div>
    </div>
  </section>

  <footer class="footer">
    <div class="footer-brand">
      <div class="brand-name">GUARDLINE</div>
      <div class="brand-tag">SITE WORKWEAR</div>
      <div class="pay" aria-label="Accepted payment methods">
        <i style="background:#e8541a"></i><i style="background:#2b6cc4"></i><i style="background:#2aa3d9"></i><i style="background:#f08f49"></i><i style="background:#2c3e8c"></i>
      </div>
    </div>
    <div class="col" style="left:446px">
      <h5>CONTACT US</h5>
      <div class="contact-row"><svg width="11" height="11" viewBox="0 0 12 12"><path d="M2 1l3 1 0 3-1.5 1a7 7 0 0 0 3 3L8 7.5h3l1 3-2 1.5C5 11 1 7 0.5 3z" fill="var(--orange)"/></svg>0400 000 123</div>
      <div class="contact-row"><svg width="12" height="10" viewBox="0 0 12 10"><rect x="0.5" y="0.5" width="11" height="9" fill="var(--orange)"/><path d="M0.5 0.5l5.5 5 5.5-5" fill="none" stroke="#1c1c1c"/></svg>info@guardlineworkwear.com</div>
      <div class="contact-row"><svg width="10" height="13" viewBox="0 0 10 13"><path d="M5 0a5 5 0 0 1 5 5c0 3-5 8-5 8S0 8 0 5a5 5 0 0 1 5-5z" fill="var(--orange)"/><circle cx="5" cy="5" r="1.8" fill="#1c1c1c"/></svg><span>Lorem Ipsum<br>Eastbrook, Vermont 05100-2200<br>United States of America</span></div>
    </div>
    <div class="col" style="left:767px">
      <h5>QUICK LINKS</h5>
      <ul><li class="current">Home</li><li>About Us</li><li>Shop</li><li>Testimonials</li><li>Contact Us</li></ul>
    </div>
    <div class="col" style="left:958px">
      <h5>POLICY</h5>
      <ul><li>Return Policy</li><li>Terms Of Use</li><li>Security</li><li>Privacy</li><li>Sitemap</li></ul>
    </div>
    <div class="subscribe">
      <h5>SUBSCRIBE TO OUR MAILING LIST</h5>
      <p>Our latest and greatest in your inbox, sign up now.</p>
      <div class="sub-form"><div class="sub-input">Enter email address...</div><div class="sub-btn">SUBSCRIBE</div></div>
    </div>
  </footer>
  <div class="bottom">
    <span>&copy; 2024 Guardline Site Workwear All Right Reserved</span>
    <div class="social"><i></i><i></i><i class="on"></i><i></i></div>
  </div>

</div>
</body>
</html>
```